Out of town New Masters of Accounting

size of ad is 7” x 9.6”
please leave one inch on bottom for footer
We want to attract out of town students to join this master's in accounting program.
You DO NOT  have to use a picture of a person.
But if you do, it should be a  male with a white shirt and should not have long hair.(look like a young executive)
THE TEXT OF THE AD IS IN THE ATTACHMENTS
THE CAP LETTERS ARE THE INSTRUCTIONS

The age we are trying to attract is from 20-30 of ages.
- a clear ad .. the text should not take up the entire ad.. it should not be very crowded -
it should be an attractive ad that people would want to see and stand out
- the text very big and take up the entire ad

```html
<!DOCTYPE html>
<html lang="en">
<head>
<meta charset="utf-8">
<title>Masters of Science in Accounting – Flyer</title>
<link href="https://fonts.googleapis.com/css2?family=Montserrat:wght@400;500;600;700;800;900&display=swap" rel="stylesheet">
<style>
  :root{
    --orange:#f7841f;
    --blue:#3b6cf0;
    --ink:#2e2e2e;
    --paper:#ffffff;
    --stage:#d9d9d9;
    --pale-orange:#fdeedf;
    --mega-blue:#3a63c9;
  }
  *{margin:0;padding:0;box-sizing:border-box}
  html,body{width:713px;height:1200px;overflow:hidden;background:var(--stage)}
  body{font-family:"Montserrat",sans-serif;color:var(--ink);position:relative}
  .flyer{position:absolute;left:0;top:110px;width:713px;height:979px;background:var(--paper);overflow:hidden}
  .shapes{position:absolute;left:0;top:0}
  .abs{position:absolute}
  .brand{left:34px;top:52px;display:flex;align-items:center;gap:8px}
  .brand-dot{width:34px;height:34px;border-radius:50%;background:var(--orange)}
  .brand-name{font-weight:700;font-size:13px;line-height:1.15;color:var(--orange)}
  .dot-field{left:6px;top:231px;width:135px;height:151px;background:var(--pale-orange)}
  .megaphone{left:540px;top:12px;width:160px;height:118px;background:linear-gradient(135deg,#6f97e8,var(--mega-blue));border-radius:40% 20% 30% 20%}
  .headline{left:165px;top:182px;width:475px;text-align:center;transform:rotate(-1deg);font-weight:900;line-height:1}
  .hl-advance{font-size:74px;color:#fff;letter-spacing:-1px}
  .hl-further{font-size:68px;color:var(--ink);letter-spacing:-1px;margin-top:2px}
  .hl-career{font-size:48px;color:#fff;font-weight:800;margin-top:6px;letter-spacing:.5px}
  .hl-sub{font-size:15px;color:#fff;font-weight:600;margin-top:10px;letter-spacing:.6px}
  .burst-text{left:30px;top:484px;width:150px;text-align:center;transform:rotate(-8deg);color:#fff;font-weight:800;line-height:1.05}
  .burst-text .b1{font-size:15px}
  .burst-text .b2{font-size:19px;color:var(--ink)}
  .burst-text .b3{font-size:12px}
  .all-new{left:33px;top:585px;font-size:44px;font-weight:800;letter-spacing:.5px}
  .remote-box{left:33px;top:643px;width:265px;height:61px;border:1px dashed var(--ink);padding:4px 10px;line-height:1.15}
  .remote-box .r1{font-size:20px;font-weight:600}
  .remote-box .r2{font-size:17px;font-weight:400;letter-spacing:.5px}
  .start{left:33px;top:710px;line-height:1.15}
  .start .s1{font-size:20px;font-weight:600;color:var(--orange)}
  .start .s2{font-size:19px;font-weight:400}
  .accolade{left:35px;top:773px;width:300px}
  .accolade .a1{font-size:18px;font-weight:700;letter-spacing:.5px}
  .accolade .a2{font-size:9.5px;line-height:1.25;margin-top:4px}
  .partner{left:357px;top:556px;white-space:nowrap}
  .partner .p1{font-size:25px;font-weight:800;color:var(--orange);letter-spacing:.3px;line-height:1.1}
  .partner .p2{font-size:17px;font-weight:600;margin-top:4px;letter-spacing:.5px;line-height:1.1}
  .perk{left:430px;font-size:13.5px;font-weight:600;letter-spacing:.3px;line-height:1.25;white-space:nowrap}
  .url{left:0;width:713px;top:840px;text-align:center;font-size:17px;font-weight:600}
  .rule{left:0;width:713px;border-top:1px dashed #555}
</style>
</head>
<body>
<main class="flyer">
  <svg class="shapes" width="713" height="979" viewBox="0 0 713 979">
    <polygon class="blue-panel" points="149,144 624,112 680,334 640,378 307,441 133,184" fill="var(--blue)" stroke="var(--blue)" stroke-width="26" stroke-linejoin="round"/>
    <path class="speech-bubble" d="M180 136 H625 Q645 136 645 156 L648 440 Q648 458 630 458 L300 445 L184 502 L210 430 L180 428 Q160 428 160 408 L163 156 Q163 136 180 136 Z" fill="var(--orange)"/>
    <polyline class="zigzag" points="555,474 571,492 587,474 603,492 619,474 635,492 651,474 667,492 683,474 699,492 713,476" fill="none" stroke="var(--blue)" stroke-width="3"/>
    <polygon class="starburst" points="105,416 118,450 150,430 146,466 185,468 158,494 192,515 155,527 170,562 136,555 128,593 105,566 82,596 74,557 38,568 53,532 16,518 50,496 26,467 64,466 58,429 92,450" fill="var(--orange)"/>
    <g class="perk-icons" fill="none" stroke="var(--orange)" stroke-width="1.5">
      <circle cx="383" cy="654" r="23"/>
      <circle cx="383" cy="722" r="23"/>
      <circle cx="383" cy="788" r="23"/>
      <g stroke="var(--ink)" stroke-width="1.3">
        <line x1="378" y1="646" x2="394" y2="646"/><line x1="378" y1="654" x2="394" y2="654"/><line x1="378" y1="662" x2="390" y2="662"/>
        <circle cx="372" cy="646" r="2"/><circle cx="372" cy="654" r="2"/><circle cx="372" cy="662" r="2"/>
        <circle cx="383" cy="716" r="5"/><path d="M373 733 Q383 720 393 733"/>
        <rect x="372" y="780" width="12" height="14"/><circle cx="392" cy="786" r="4"/><line x1="375" y1="785" x2="381" y2="785"/><line x1="375" y1="789" x2="381" y2="789"/>
      </g>
    </g>
  </svg>

  <div class="abs brand"><span class="brand-dot"></span><span class="brand-name">Gradscope<br>Ranking</span></div>
  <div class="abs dot-field" role="img" aria-label="Decorative orange dot grid"></div>
  <div class="abs megaphone" role="img" aria-label="Illustration of a hand holding a blue megaphone"></div>

  <h1 class="abs headline">
    <div class="hl-advance">ADVANCE</div>
    <div class="hl-further">FURTHER</div>
    <div class="hl-career">IN YOUR CAREER</div>
    <div class="hl-sub">WITH A MASTERS OF SCIENCE IN ACCOUNTING</div>
  </h1>

  <div class="abs burst-text"><div class="b1">A MASTERS</div><div class="b2">IN ONLY</div><div class="b3">15 MONTHS</div></div>

  <div class="abs all-new">ALL NEW!</div>
  <div class="abs remote-box"><div class="r1">Remote program For</div><div class="r2">out of town students</div></div>
  <div class="abs start"><div class="s1">Beginning August 17</div><div class="s2">New lower prices</div></div>
  <div class="abs accolade">
    <div class="a1">GRADSCOPE</div>
    <div class="a2">Northbrook University (NBU) Master in Accounting Program Received the highest possible star rating</div>
  </div>

  <div class="abs partner"><div class="p1">LAKEVIEW CAREERS</div><div class="p2">JOB PLACEMENT ADVANTAGE</div></div>
  <div class="abs perk" style="top:646px">96% PLACEMENT RATE</div>
  <div class="abs perk" style="top:714px">8 PLACEMENT COORDINATORS</div>
  <div class="abs perk" style="top:771px">DECADES OF RELATIONSHIPS<br>WITH 100'S OF FIRM</div>

  <div class="abs url">www.grad-ledger.us</div>
  <div class="abs rule" style="top:877px"></div>
  <div class="abs rule" style="top:969px"></div>
</main>
</body>
</html>
```